New National Dermatology Group needs a business card!

We need a business card for our new national company that has 3 brands within the business:
Brindlewood Clinics Australia, Harrowmere Clinics Australia and Tallowfen Clinics Australia.
We help people access dermatology services close to home throughout Australia.
We need a business card that has:
all 3 logos on it,
Our websites (there are three, listed above)
Our email (there are three, listed above)
The location of our first clinic: 41 Wren St Parramatta (this can then be changed for each location as required)

```html
<!DOCTYPE html>
<html lang="en">
<head>
<meta charset="utf-8">
<title>Dermatology Group Business Card</title>
<link href="https://fonts.googleapis.com/css2?family=Arimo:wght@400&display=swap" rel="stylesheet">
<style>
:root{
  --backdrop:#b7b7b7;
  --card:#ffffff;
  --ink:#1e1e1e;
  --brown:#7a3f1d;
  --green:#21a84a;
  --orange:#f6862a;
  --shadow:rgba(0,0,0,.55);
}
*{margin:0;padding:0;box-sizing:border-box}
html,body{width:1075px;height:1200px;overflow:hidden}
body{background:var(--backdrop);position:relative;font-family:"Arimo",Arial,sans-serif;color:var(--ink)}
.card{position:absolute;left:206px;width:664px;height:396px;background:var(--card);box-shadow:3px 3px 2px var(--shadow);overflow:hidden}
.card--front{top:187px}
.card--back{top:638px}
.band{position:absolute;left:0;width:100%;height:29px;display:flex}
.band--top{top:0}
.band--bottom{bottom:0}
.band__part{flex:1}
.band__part--brown{background:var(--brown)}
.band__part--green{background:var(--green)}
.band__part--orange{background:var(--orange)}
.contacts{position:absolute;left:35px}
.contact{list-style:none;color:var(--accent)}
.contact__line{display:flex;align-items:center;height:23px;font-size:18px;color:var(--ink);white-space:nowrap}
.contact__line--addr{margin-top:7px}
.contact__line svg{width:17px;height:17px;margin-right:8px;flex:none;fill:var(--accent)}
.contact__line .hl{color:var(--accent)}
.contact--brown{--accent:var(--brown);top:55px}
.contact--green{--accent:var(--green);top:148px}
.contact--orange{--accent:var(--orange);top:242px}
.brand{position:absolute;text-align:center;color:var(--accent);font-weight:400;line-height:1}
.brand__name{display:block;text-transform:uppercase;letter-spacing:1px}
.brand__sub{display:block;text-transform:uppercase}
.brand--brown{--accent:var(--brown)}
.brand--green{--accent:var(--green)}
.brand--orange{--accent:var(--orange)}
.card--front .brand{left:410px;width:214px}
.card--front .brand__name{font-size:29px}
.card--front .brand__sub{font-size:10px;letter-spacing:4.2px;margin-top:4px}
.card--back .brand{left:202px;width:260px}
.card--back .brand__name{font-size:36px}
.card--back .brand__sub{font-size:12px;letter-spacing:5.2px;margin-top:5px}
</style>
</head>
<body>

<section class="card card--front">
  <ul class="contact contacts contact--brown">
    <li class="contact__line"><svg viewBox="0 0 20 20"><path d="M1 4h18v12H1z M1 4l9 7 9-7" stroke="#fff" stroke-width="1.2"/></svg>info@webname.com</li>
    <li class="contact__line"><svg viewBox="0 0 20 20"><circle cx="10" cy="10" r="9"/><path d="M1 10h18M10 1v18M3 5.5h14M3 14.5h14M10 1c-5 5-5 13 0 18M10 1c5 5 5 13 0 18" stroke="#fff" stroke-width="1" fill="none"/></svg>www.<span class="hl">websitename</span>.com</li>
    <li class="contact__line contact__line--addr"><svg viewBox="0 0 20 20"><path d="M10 1a6.5 6.5 0 0 0-6.5 6.5C3.5 12 10 19 10 19s6.5-7 6.5-11.5A6.5 6.5 0 0 0 10 1z"/><circle cx="10" cy="7.5" r="2.4" fill="#fff"/></svg>41 Wren St Parramatta</li>
  </ul>
  <ul class="contact contacts contact--green">
    <li class="contact__line"><svg viewBox="0 0 20 20"><path d="M1 4h18v12H1z M1 4l9 7 9-7" stroke="#fff" stroke-width="1.2"/></svg>info@webname.com</li>
    <li class="contact__line"><svg viewBox="0 0 20 20"><circle cx="10" cy="10" r="9"/><path d="M1 10h18M10 1v18M3 5.5h14M3 14.5h14M10 1c-5 5-5 13 0 18M10 1c5 5 5 13 0 18" stroke="#fff" stroke-width="1" fill="none"/></svg>www.<span class="hl">websitename</span>.com</li>
    <li class="contact__line contact__line--addr"><svg viewBox="0 0 20 20"><path d="M10 1a6.5 6.5 0 0 0-6.5 6.5C3.5 12 10 19 10 19s6.5-7 6.5-11.5A6.5 6.5 0 0 0 10 1z"/><circle cx="10" cy="7.5" r="2.4" fill="#fff"/></svg>41 Wren St Parramatta</li>
  </ul>
  <ul class="contact contacts contact--orange">
    <li class="contact__line"><svg viewBox="0 0 20 20"><path d="M1 4h18v12H1z M1 4l9 7 9-7" stroke="#fff" stroke-width="1.2"/></svg>info@webname.com</li>
    <li class="contact__line"><svg viewBox="0 0 20 20"><circle cx="10" cy="10" r="9"/><path d="M1 10h18M10 1v18M3 5.5h14M3 14.5h14M10 1c-5 5-5 13 0 18M10 1c5 5 5 13 0 18" stroke="#fff" stroke-width="1" fill="none"/></svg>www.<span class="hl">websitename</span>.com</li>
    <li class="contact__line contact__line--addr"><svg viewBox="0 0 20 20"><path d="M10 1a6.5 6.5 0 0 0-6.5 6.5C3.5 12 10 19 10 19s6.5-7 6.5-11.5A6.5 6.5 0 0 0 10 1z"/><circle cx="10" cy="7.5" r="2.4" fill="#fff"/></svg>41 Wren St Parramatta</li>
  </ul>

  <div class="brand brand--brown" style="top:68px"><span class="brand__name">Tallowfen</span><span class="brand__sub">Clinics Australia</span></div>
  <div class="brand brand--green" style="top:168px"><span class="brand__name">Brindlewood</span><span class="brand__sub">Clinics Australia</span></div>
  <div class="brand brand--orange" style="top:272px"><span class="brand__name">Harrowmere</span><span class="brand__sub">Clinics Australia</span></div>

  <div class="band band--bottom" role="img" aria-label="Decorative border pattern in brown, green and orange">
    <span class="band__part band__part--brown"></span><span class="band__part band__part--green"></span><span class="band__part band__part--orange"></span>
  </div>
</section>

<section class="card card--back">
  <div class="band band--top" role="img" aria-label="Decorative border pattern in brown, green and orange">
    <span class="band__part band__part--brown"></span><span class="band__part band__part--green"></span><span class="band__part band__part--orange"></span>
  </div>

  <div class="brand brand--brown" style="top:72px"><span class="brand__name">Tallowfen</span><span class="brand__sub">Clinics Australia</span></div>
  <div class="brand brand--green" style="top:172px"><span class="brand__name">Brindlewood</span><span class="brand__sub">Clinics Australia</span></div>
  <div class="brand brand--orange" style="top:278px"><span class="brand__name">Harrowmere</span><span class="brand__sub">Clinics Australia</span></div>

  <div class="band band--bottom" role="img" aria-label="Decorative border pattern in brown, green and orange">
    <span class="band__part band__part--brown"></span><span class="band__part band__part--green"></span><span class="band__part band__part--orange"></span>
  </div>
</section>

</body>
</html>
```